Medical Device Packaging Project 3 of 5

We are a medical device startup company needing packaging for a total of 5 device brands. This is posting 3 of 5 and the device name is "Venor"

Venor is an intraocular lens for use in cataract surgery. The target market is Chinese ophthalmologists. The box should be sophisticated and upmarket.

The company name is Tamsin Medica, I have included the logo in the uploaded files section. You should include the logo on the box.

I have uploaded a sample lens boxes from other companies that demonstrate the information needed to be contained on the box in terms of address, warnings, symbols, etc.

I have also uploaded the blank dieline of the boxes

You are welcome and encouraged to also submit to projects 1, 2, 4, and 5 as well. The same rules and expectations apply.

Requirements
Should not have
• Should not have any images of an eye or any bionic/futuristic feel to the design
• Note that the calvoptix box is for text reference only. You may use the lens image but the futuristic/bionic look is NOT what we are going for with this brand. It should be traditional upmarket medical device artwork.

```html
<!DOCTYPE html>
<html lang="en">
<head>
<meta charset="utf-8">
<title>Venor – Hydrophobic Intraocular Lens Packaging</title>
<link rel="stylesheet" href="https://fonts.googleapis.com/css2?family=Montserrat:wght@400;500;600&family=Arimo:wght@400&display=swap">
<style>
  :root {
    --stage: #e4e4e4;
    --panel-top: #ffffff;
    --mint: #9fe3d2;
    --mint-deep: #6fd2bb;
    --title-green: #2f6b5c;
    --brand-navy: #173a7a;
    --brand-ring: #9ccbe8;
    --body-grey: #4a4a4a;
    --lens-light: #e6e6e6;
    --lens-dark: #6e6e6e;
    --icon: #555555;
  }
  * { box-sizing: border-box; margin: 0; padding: 0; }
  html, body { width: 1200px; height: 782px; overflow: hidden; }
  body {
    background: radial-gradient(ellipse at center, #f4f4f4 0%, var(--stage) 100%);
    font-family: "Montserrat", sans-serif;
    position: relative;
  }
  .panel {
    position: absolute;
    top: 180px;
    width: 520px;
    height: 420px;
    overflow: hidden;
    background:
      radial-gradient(ellipse 70% 45% at 45% 78%, rgba(111,210,187,0.55), transparent 70%),
      radial-gradient(ellipse 60% 35% at 80% 60%, rgba(159,227,210,0.5), transparent 70%),
      linear-gradient(180deg, var(--panel-top) 0%, #eef9f6 35%, var(--mint) 75%, #c9efe5 100%);
    box-shadow: 0 14px 30px rgba(0,0,0,0.12);
  }
  .panel--back { left: 50px; }
  .panel--front { left: 630px; }

  .brand {
    position: absolute;
    top: 96px;
    left: 32px;
    display: flex;
    align-items: center;
    gap: 9px;
  }
  .brand__dot {
    width: 12px; height: 12px;
    border-radius: 50%;
    background: var(--brand-ring);
  }
  .brand__name {
    font-weight: 500;
    font-size: 20px;
    letter-spacing: 1px;
    color: var(--brand-navy);
    white-space: nowrap;
  }

  .product-title {
    position: absolute;
    right: 28px;
    top: 40px;
    text-align: right;
    font-weight: 500;
    font-size: 14px;
    line-height: 1.4;
    letter-spacing: 0.3px;
    color: var(--title-green);
    text-transform: uppercase;
    white-space: nowrap;
  }

  .lens-art {
    position: absolute;
    background: radial-gradient(circle at 45% 40%, var(--lens-light) 0%, #b8b8b8 45%, var(--lens-dark) 100%);
    border-radius: 50%;
  }
  .panel--back .lens-art { left: 340px; top: 140px; width: 140px; height: 140px; opacity: 0.9; }
  .panel--front .lens-art { left: 290px; top: 120px; width: 190px; height: 190px; opacity: 0.9; }

  .warnings {
    position: absolute;
    left: 32px;
    top: 168px;
    width: 280px;
    font-family: "Arimo", sans-serif;
    font-size: 7px;
    line-height: 1.15;
    color: var(--body-grey);
  }
  .warnings p { margin-bottom: 4px; }

  .symbols {
    position: absolute;
    right: 26px;
    bottom: 24px;
    display: flex;
    align-items: center;
    gap: 7px;
  }
  .symbols .sterile {
    display: flex;
    border: 1px solid var(--icon);
    font-family: "Arimo", sans-serif;
    font-size: 6px;
    color: var(--icon);
  }
  .symbols .sterile span { padding: 2px 3px; }
  .symbols .sterile span + span { border-left: 1px solid var(--icon); }

  .device-name {
    position: absolute;
    left: 30px;
    bottom: 34px;
    color: var(--title-green);
  }
  .device-name__name {
    font-weight: 600;
    font-size: 22px;
    letter-spacing: 5px;
    text-transform: uppercase;
    line-height: 1.1;
  }
  .device-name__sub {
    font-weight: 500;
    font-size: 14px;
    letter-spacing: 0.3px;
    text-transform: uppercase;
  }
</style>
</head>
<body>

<section class="panel panel--back" aria-label="Back panel">
  <div class="brand"><span class="brand__dot"></span><span class="brand__name">Tamsin Medica</span></div>
  <h2 class="product-title">Hydrophobic Intraocular Lens<br>Aspheric with 360° Lens</h2>

  <div class="warnings">
    <p>Contains one sterile intraocular lens<br>Do not use if the packaging is damaged<br>Do not resterilize</p>
    <p>Bevat één steriele intraoculaire lens<br>Niet gebruiken als de verpakking beschadigd is<br>Niet opnieuw steriliseren</p>
    <p>Contient une lentille intraoculaire stérile<br>Ne pas utiliser si l'emballage est endommagé<br>Ne pas restériliser</p>
    <p>Enthält eine sterile intraokulare Linse<br>Nicht verwenden, wenn die Verpackung beschädigt ist<br>Nicht resterilisieren</p>
    <p>Περιέχει ένα αποστειρωμένο ενδοφθάλμιο φακό<br>Μην το χρησιμοποιείτε εάν η συσκευασία έχει υποστεί ζημιά<br>Μην επαναποστειρώνετε</p>
    <p>Contiene una lente intraoculare sterile<br>Non usare se la confezione è danneggiata<br>Non risterilizzare</p>
    <p>Contém uma lente intra-ocular esterilizada<br>Não use se a embalagem está danificada<br>Não reesterilize</p>
    <p>Contiene una lente intraocular estéril<br>No utilizar si el envase está dañado<br>No vuelva a esterilizar</p>
  </div>

  <div class="lens-art" role="img" aria-label="Illustration of a grey intraocular lens with two curved haptics"></div>

  <div class="symbols" aria-label="Regulatory symbols">
    <div class="sterile"><span>STERILE</span><span>EO</span></div>
    <svg width="14" height="13" viewBox="0 0 14 13" aria-hidden="true"><path d="M7 1 L13 12 L1 12 Z" fill="none" stroke="#555" stroke-width="1"/><path d="M7 5 V9" stroke="#555"/></svg>
    <svg width="14" height="14" viewBox="0 0 14 14" aria-hidden="true"><circle cx="7" cy="7" r="6" fill="none" stroke="#555"/><text x="7" y="10" font-size="8" text-anchor="middle" fill="#555" font-family="Arimo, sans-serif">2</text><path d="M3 11 L11 3" stroke="#555"/></svg>
    <svg width="14" height="14" viewBox="0 0 14 14" aria-hidden="true"><circle cx="7" cy="7" r="6" fill="none" stroke="#555"/><path d="M3 11 L11 3" stroke="#555"/></svg>
    <svg width="14" height="14" viewBox="0 0 14 14" aria-hidden="true"><circle cx="7" cy="7" r="6" fill="none" stroke="#555"/><rect x="4" y="5" width="6" height="4" fill="none" stroke="#555"/><path d="M3 11 L11 3" stroke="#555"/></svg>
  </div>
</section>

<section class="panel panel--front" aria-label="Front panel">
  <div class="brand"><span class="brand__dot"></span><span class="brand__name">Tamsin Medica</span></div>
  <h2 class="product-title">Hydrophobic Intraocular Lens</h2>

  <div class="lens-art" role="img" aria-label="Illustration of a grey intraocular lens with two curved haptics"></div>

  <div class="device-name">
    <div class="device-name__name">Venor</div>
    <div class="device-name__sub">Aspheric with 360° Lens</div>
  </div>
</section>

</body>
</html>
```